An magic noodle needs an packing and logo design

We need a packing and logo design for an amazing noodle named Slurpio, which is a series of low-calorie noodles with zero net carbs are made out of water-soluble dietary fiber made from the natural Konjac. Not only are they yummy, but Slurpio are able to satisfy your hunger just like regular noodles and you will find yourself losing weight magically with enjoying delicious food.
Updates

Project Deadline Extended Reason: Some designer applied awaiting and said their design will come soon. Added Wednesday, July 12, 2017

Target Market(s)

Somebody who seeks a healthy and yummy meal to keep fit or lose weight.

Logo Text

Slurpio

Requirements
Must have
• The front side:
• Logo
• Low-calorie, Low-carb, Low Cholesterol, Gluten free, Good Source of Fiber, Gluten Free, Dairy Free, NON-GMO
• 纯天然高纤低脂面
• Tomato flavor, 68 Cal
• Ready to enjoy 1 min, Pre-cooked meal
• A brief description for Konjac glucomannan (Konjac glucomannan is the best natural soluble dietary fiber.
• The Northfield Nutrition Council recommends a healthy diet including 25-38 grams of fiber per day.)
• The back side:
• Storage instructions
• Cooking instructions
• The story: Konjac, which is also called “Moyu”, “Juro” or “Shirataki”, belongs to Araceae, and it’s the only perennial plant that can provide a large amount of glucomannan. Konjac fiber, as known as glucomannan, is a kind of good water-soluble dietary fiber, and is given the name of “The seventh nutrient”, “Blood purification agent”.
• The beneficial dietary fiber derived from the organic Konjac root, which is native to Asia, especially Shaanxi of China, where is the home of wild giant pandas and is richly endowed with varied landforms and a complex ecosystem containing many rare animals and plants. This national nature reserve has been described as the “Natural Animal and Plant Gene Base”.)
• Nutrition Facts
• The dimension of old vision is 380*195mm and the material will be aluminum foil. But the dimension is adjustable if the designer has a better opinion. The food in the packaging is one meal. I have uploaded the previous packaging and the one from the same industry.
Nice to have
• The figure of great panda

```html
<!DOCTYPE html>
<html lang="en">
<head>
<meta charset="utf-8">
<title>Slurpio – Tomato Flavor Pack Front</title>
<link rel="stylesheet" href="https://fonts.googleapis.com/css2?family=Josefin+Slab:wght@400&family=Mulish:wght@400;500&family=Roboto+Condensed:wght@300;400&display=swap">
<style>
  :root{
    --stage:#8f8f8f;
    --pack-white:#f4f4f4;
    --ink:#2b2b2b;
    --lime:#8cc63f;
    --lime-bright:#b5e23a;
    --green-icon:#6aaa1e;
    --gold:#d9b23a;
    --gold-light:#f2dc7a;
    --panel-dark:#6b6759;
    --panel-mid:#8d8877;
    --tile:#6f6b5f;
    --noodle-a:#efe2bf;
    --noodle-b:#d9b978;
  }
  *{box-sizing:border-box;margin:0;padding:0}
  html,body{width:1054px;height:1200px;overflow:hidden}
  body{background:var(--stage);position:relative;font-family:"Mulish",sans-serif;color:var(--ink)}

  .pack{position:absolute;left:168px;top:84px;width:766px;height:1048px;background:var(--pack-white);overflow:hidden}
  .pack-art{position:absolute;inset:0}

  .noodle-strip{position:absolute;background:linear-gradient(135deg,var(--noodle-a),var(--noodle-b) 55%,var(--noodle-a))}
  .noodle-strip.top{left:0;top:0;width:766px;height:210px}
  .noodle-strip.bottom{left:0;top:860px;width:766px;height:188px}

  .brand{position:absolute;left:166px;top:52px;width:439px;text-align:center}
  .brand-name{font-family:"Mulish",sans-serif;font-weight:500;font-size:66px;line-height:1;color:var(--lime-bright);letter-spacing:1px}
  .brand-tagline{margin:14px auto 0;width:226px;border-top:1px solid #d8d5c8;padding-top:6px;font-size:12px;font-weight:500;color:#f2f2f2;letter-spacing:.2px}

  .rule{position:absolute;height:1px;background:var(--ink)}
  .title-bars{position:absolute;left:364px;top:234px;width:44px;height:32px;
    background:repeating-linear-gradient(90deg,var(--lime) 0 3px,transparent 3px 6px)}
  .product-name{position:absolute;left:100px;top:250px;width:566px;text-align:center;font-family:"Josefin Slab",serif;font-weight:400;font-size:116px;line-height:1;letter-spacing:-1px}
  .flavor{position:absolute;left:100px;top:370px;width:566px;text-align:center;font-size:27px;line-height:1}
  .prep{position:absolute;left:100px;top:428px;width:566px;text-align:center;font-size:26px;line-height:1;white-space:nowrap}

  .claims{position:absolute;left:188px;top:478px;width:390px;height:110px}
  .claim{position:absolute;width:120px;text-align:center;font-family:"Roboto Condensed",sans-serif;font-size:20px;color:var(--green-icon);white-space:nowrap}
  .claim svg{display:block;margin:0 auto 14px}

  .dish-photo{position:absolute;left:136px;top:610px;width:496px;height:238px;border-radius:50% 50% 12px 12px / 40% 40% 12px 12px;
    background:radial-gradient(ellipse at 50% 45%,#e9f1d6 0,#f2e4bd 35%,#e7c98c 60%,#d95a3a 82%,#f2f2f2 100%)}

  .benefit-panel{position:absolute;left:166px;top:848px;width:439px;height:200px}
  .benefit{position:absolute;width:154px;height:45px;background:var(--tile);display:flex;align-items:center;white-space:nowrap;
    font-family:"Roboto Condensed",sans-serif;font-weight:300;font-size:15px;color:#f1f1f1}
  .benefit .plus{flex:none;width:28px;height:45px;margin-right:10px;background:linear-gradient(180deg,var(--lime-bright),#c9d62a);
    display:flex;align-items:center;justify-content:center;font-size:22px;color:#fff;font-weight:300}
</style>
</head>
<body>
  <main class="pack">
    <div class="noodle-strip top" role="img" aria-label="Close-up photo of konjac noodles"></div>
    <div class="noodle-strip bottom" role="img" aria-label="Close-up photo of konjac noodles"></div>

    <svg class="pack-art" width="766" height="1048" viewBox="0 0 766 1048" aria-hidden="true">
      <defs>
        <linearGradient id="gold" x1="0" y1="0" x2="1" y2="0">
          <stop offset="0" stop-color="#c99a2a"/><stop offset=".5" stop-color="#f2dc7a"/><stop offset="1" stop-color="#c99a2a"/>
        </linearGradient>
        <linearGradient id="lime" x1="0" y1="0" x2="1" y2="0">
          <stop offset="0" stop-color="#7dbb2c"/><stop offset="1" stop-color="#b5e23a"/>
        </linearGradient>
      </defs>
      <path d="M20 230 L166 200 L383 228 L600 200 L746 230 L746 880 L20 880 Z" fill="#f4f4f4"/>
      <path d="M0 160 L166 140 L166 175 L0 200 Z" fill="url(#gold)"/>
      <path d="M0 200 L166 175 L166 200 L20 230 L0 232 Z" fill="url(#lime)"/>
      <path d="M766 160 L600 140 L600 175 L766 200 Z" fill="url(#gold)"/>
      <path d="M766 200 L600 175 L600 200 L746 230 L766 232 Z" fill="url(#lime)"/>
      <path d="M0 800 L130 830 L166 880 L0 870 Z" fill="url(#gold)"/>
      <path d="M0 830 L150 860 L166 900 L0 895 Z" fill="url(#lime)"/>
      <path d="M766 820 L600 860 L600 885 L766 860 Z" fill="url(#gold)"/>
      <path d="M766 860 L600 885 L600 905 L766 900 Z" fill="url(#lime)"/>
      <path d="M166 0 L605 0 L605 190 L383 228 L166 190 Z" fill="#6b6759"/>
      <path d="M166 895 L383 848 L605 895 L605 1048 L166 1048 Z" fill="#8d8877"/>
    </svg>

    <header class="brand">
      <p class="brand-name">Moriva</p>
      <p class="brand-tagline">KONJAC PRODUCTS ALL IN MORIVA</p>
    </header>

    <div class="rule" style="left:144px;top:244px;width:210px"></div>
    <div class="rule" style="left:418px;top:244px;width:206px"></div>
    <div class="title-bars"></div>
    <h1 class="product-name">Slurpio</h1>
    <p class="flavor">Tomato flavor, 68 Cal</p>
    <div class="rule" style="left:144px;top:418px;width:500px"></div>
    <p class="prep">Ready to enjoy 1 min, Pre-cooked meal</p>

    <section class="claims">
      <div class="claim" style="left:-13px;top:-6px">
        <svg width="72" height="72" viewBox="0 0 72 72"><circle cx="36" cy="36" r="33" fill="none" stroke="currentColor" stroke-width="3"/>
          <path d="M36 56 V30 M36 36 C28 34 24 26 26 18 C33 20 37 27 36 36 M36 32 C42 28 48 28 52 24 C50 32 44 36 36 36" fill="none" stroke="currentColor" stroke-width="3"/>
          <line x1="14" y1="14" x2="58" y2="58" stroke="currentColor" stroke-width="3"/></svg>
        Non-GMO
      </div>
      <div class="claim" style="left:118px;top:-6px">
        <svg width="72" height="72" viewBox="0 0 72 72"><circle cx="36" cy="36" r="33" fill="none" stroke="currentColor" stroke-width="3"/>
          <path d="M36 58 V16 M36 24 l-7 -5 M36 24 l7 -5 M36 34 l-8 -5 M36 34 l8 -5 M36 44 l-8 -5 M36 44 l8 -5" fill="none" stroke="currentColor" stroke-width="4" stroke-linecap="round"/>
          <line x1="14" y1="14" x2="58" y2="58" stroke="currentColor" stroke-width="3"/></svg>
        Gluten Free
      </div>
      <div class="claim" style="left:249px;top:-6px">
        <svg width="72" height="72" viewBox="0 0 72 72"><circle cx="36" cy="36" r="33" fill="none" stroke="currentColor" stroke-width="3"/>
          <path d="M32 12 h8 v8 l6 8 v30 h-20 v-30 l6 -8 z" fill="currentColor"/>
          <line x1="14" y1="14" x2="58" y2="58" stroke="currentColor" stroke-width="3"/></svg>
        Diary Free
      </div>
    </section>

    <div class="dish-photo" role="img" aria-label="Photo of a plate of noodles topped with cucumber strips, tomato slices and coriander"></div>

    <section class="benefit-panel">
      <div class="benefit" style="left:50px;top:32px"><span class="plus">+</span>Low-calorie</div>
      <div class="benefit" style="left:218px;top:32px;width:170px"><span class="plus">+</span>Low-carb</div>
      <div class="benefit" style="left:50px;top:88px"><span class="plus">+</span>Low Cholesterol</div>
      <div class="benefit" style="left:218px;top:88px;width:170px"><span class="plus">+</span>Good Source of Fiber</div>
    </section>
  </main>
</body>
</html>
```